Owen Tasker Studios Business Card

Looking for a clear, modern, elegant, sharp business card that conveys a professional yet edgy image to my business as a wedding, portrait, and travel photographer. Would like something that looks vintage yet modern. Need a new business card to grow my business. We are growing the business for Wedding and Event Photography as well as fine art Photography. (Mostly Landscapes)
Updates

I’m looking through designs now but I have a new logo that i want using please.

New logo uploaded please redesign using that

PLEASE ALL DESIGNERS LOOK IN BRIEF FOR NEW LOGO

Target Market(s)

Brides, Grooms, Families with Kids, People looking for Fine Art Photography Artwork

Industry/Entity Type

Photographer

Contact Information for Business Card

Unsure

Font styles to use
Serif

Colors

Designer to choose colors to be used in the design.

Requirements
Must have
• My Website:
• http://taskerlens.examplefolio.net
• Phone:
• 323-481-5206
• Email:
• owentaskerlens@mailbox-example.net
Nice to have
• Would like a sort of shine on the printing finish.
• I like black I think it looks good on a business card.
• Can try working with my logo (png that I've attached)

```html
<!DOCTYPE html>
<html lang="en">
<head>
<meta charset="utf-8">
<title>Owen Tasker Studios Business Card</title>
<link rel="stylesheet" href="https://fonts.googleapis.com/css2?family=Montserrat:wght@300;400&family=Questrial&display=swap">
<style>
  :root {
    --backdrop: #3a3633;
    --card-black: #141414;
    --card-edge: #1e1e1e;
    --foil-silver: #8f8f8f;
    --foil-dim: #5f5f5f;
    --ink-white: #f2f2f2;
    --ink-soft: #d9d9d9;
  }
  * { box-sizing: border-box; margin: 0; padding: 0; }
  html, body { width: 1200px; height: 780px; overflow: hidden; }
  body {
    background: var(--backdrop);
    display: flex;
    align-items: center;
    justify-content: center;
    gap: 60px;
  }
  .card {
    width: 500px;
    height: 286px;
    background: radial-gradient(ellipse at 40% 30%, #1d1d1d 0%, var(--card-black) 70%);
    border: 1px solid var(--card-edge);
    border-radius: 3px;
    position: relative;
  }
  .card-front {
    display: flex;
    flex-direction: column;
    align-items: center;
    justify-content: center;
  }
  .studio-name {
    font-family: "Montserrat", sans-serif;
    font-weight: 300;
    font-size: 30px;
    letter-spacing: 0.32em;
    color: var(--foil-silver);
    padding-left: 0.32em;
  }
  .studio-tag {
    font-family: "Montserrat", sans-serif;
    font-weight: 300;
    font-size: 9px;
    letter-spacing: 0.5em;
    color: var(--foil-silver);
    margin-top: 6px;
    padding-left: 0.5em;
  }
  .card-back .contact {
    position: absolute;
    right: 40px;
    top: 118px;
    text-align: right;
    font-family: "Questrial", sans-serif;
    color: var(--ink-soft);
  }
  .contact-name {
    font-size: 17px;
    color: var(--ink-white);
    letter-spacing: 0.02em;
  }
  .contact-role {
    font-size: 11px;
    margin-bottom: 6px;
  }
  .contact-line {
    font-size: 12.5px;
    line-height: 1.45;
  }
</style>
</head>
<body>
  <section class="card card-front" aria-label="Card front">
    <div class="studio-name">OWEN TASKER</div>
    <div class="studio-tag">STUDIOS</div>
  </section>

  <section class="card card-back" aria-label="Card back">
    <div class="contact">
      <div class="contact-name">OWEN TASKER</div>
      <div class="contact-role">Photographer</div>
      <div class="contact-line">P: 323-481-5206 | E: owentaskerlens@mailbox-example.net</div>
      <div class="contact-line">http://taskerlens.examplefolio.net</div>
    </div>
  </section>
</body>
</html>
```